KEEN Holdings Bowling Invite

Fun Bowling Invite that can be printed or shared digitally. KEEN Holdings wouldnt be what it is today without the dedication of our outstanding employees that help us throughout the year. We also acknowledge that our shifts often vary which affects those at home. We graciously invite you and your family to join us for Bowling, Pizza and Drinks.

Target Market(s)

Company Employees and their families

Industry/Entity Type

Trucking and Excavating

Font styles to use
Sans Serif

Colors
EB3D1F
EC4F4E
F09395
F8D3D4
FCEDEE

Requirements
Must have
• "Bowling with the KEEN" could be a slogan or something along that lines. The event will be Sunday, April 23rd from 3:30PM - 5:30 PM. will be held at Tamarlind Bowling Alley 4817 Corvell Street Green Bay, WI 58216.
Nice to have
• Include the brief description showing our appreciation to our employees.
Should not have
• .

```html
<!DOCTYPE html>
<html lang="en">
<head>
<meta charset="utf-8">
<title>KEEN Holdings Bowling Invite</title>
<link href="https://fonts.googleapis.com/css2?family=Montserrat:wght@300;400;700&family=Roboto:wght@500&display=swap" rel="stylesheet">
<style>
  :root {
    --red: #eb3d1f;
    --coral: #ec4f4e;
    --rose: #f09395;
    --blush: #f8d3d4;
    --mist: #fcedee;
    --ink: #1a1a1a;
    --paper: #ffffff;
  }
  html, body {
    margin: 0;
    padding: 0;
    width: 1200px;
    height: 1200px;
    overflow: hidden;
    background: var(--paper);
  }
  .invite {
    position: relative;
    width: 1200px;
    height: 1200px;
    overflow: hidden;
    background: var(--paper);
    font-family: "Montserrat", sans-serif;
    color: var(--ink);
  }
  .decor {
    position: absolute;
    inset: 0;
  }
  .headline {
    position: absolute;
    top: 290px;
    left: 0;
    width: 100%;
    text-align: center;
    margin: 0;
    color: var(--red);
  }
  .headline__lead {
    display: block;
    font-weight: 400;
    font-size: 92px;
    line-height: 108px;
  }
  .headline__name {
    display: block;
    font-weight: 700;
    font-size: 116px;
    line-height: 156px;
    letter-spacing: 2px;
  }
  .event-date {
    position: absolute;
    top: 575px;
    left: 0;
    width: 100%;
    text-align: center;
    margin: 0;
    font-family: "Roboto", sans-serif;
    font-weight: 500;
    font-size: 60px;
    line-height: 70px;
    color: var(--coral);
  }
  .event-details {
    position: absolute;
    top: 680px;
    left: 0;
    width: 100%;
    text-align: center;
    margin: 0;
    font-weight: 300;
    font-size: 18px;
    line-height: 28px;
  }
  .message {
    position: absolute;
    top: 820px;
    left: 0;
    width: 100%;
    text-align: center;
    font-weight: 400;
    font-size: 18.5px;
    line-height: 38.5px;
  }
  .message p { margin: 0; }
  .message .message__invite { margin-top: 37px; }
</style>
</head>
<body>
<main class="invite">
  <svg class="decor" width="1200" height="1200" viewBox="0 0 1200 1200">
    <defs>
      <linearGradient id="pin-fill" x1="0" y1="0" x2="0" y2="1">
        <stop offset="0" stop-color="#fcedee"/>
        <stop offset="1" stop-color="#f8d3d4"/>
      </linearGradient>
    </defs>

    <g class="bowling-pin" role="img" aria-label="Bowling pin illustration">
      <rect x="-52" y="-165" width="104" height="330" rx="52" fill="url(#pin-fill)" transform="translate(70 345) rotate(22)"/>
    </g>
    <g class="bowling-pin" role="img" aria-label="Bowling pin illustration">
      <rect x="-52" y="-155" width="104" height="310" rx="52" fill="url(#pin-fill)" transform="translate(1130 295) rotate(-38)"/>
    </g>
    <g class="bowling-pin" role="img" aria-label="Bowling pin illustration">
      <rect x="-60" y="-160" width="120" height="320" rx="60" fill="url(#pin-fill)" transform="translate(165 1040) rotate(-22)"/>
    </g>
    <g class="bowling-pin" role="img" aria-label="Bowling pin illustration">
      <rect x="-50" y="-140" width="100" height="280" rx="50" fill="url(#pin-fill)" transform="translate(1110 980) rotate(32)"/>
    </g>

    <circle class="bowling-ball" role="img" aria-label="Bowling ball illustration" cx="372" cy="-12" r="104" fill="var(--blush)"/>
    <circle class="bowling-ball" role="img" aria-label="Bowling ball illustration" cx="790" cy="175" r="60" fill="var(--blush)"/>
    <circle class="bowling-ball" role="img" aria-label="Bowling ball illustration" cx="173" cy="677" r="59" fill="var(--blush)"/>
    <circle class="bowling-ball" role="img" aria-label="Bowling ball illustration" cx="1185" cy="693" r="82" fill="var(--blush)"/>
    <circle class="bowling-ball" role="img" aria-label="Bowling ball illustration" cx="928" cy="1170" r="56" fill="var(--blush)"/>
  </svg>

  <h1 class="headline">
    <span class="headline__lead">Bowling with the</span>
    <span class="headline__name">K.E.E.N.</span>
  </h1>

  <p class="event-date">Sunday, April 23</p>

  <p class="event-details">3:30PM - 5:30 PM<br>Tamarlind Bowling Alley<br>4817 Corvell Street, Green Bay, WI 58216</p>

  <section class="message">
    <p>KEEN Holdings wouldnt be what it is today without the dedication of our</p>
    <p>outstanding employees that help us throughout the year.</p>
    <p>We also acknowledge that our shifts often vary</p>
    <p>which affects those at home.</p>
    <p class="message__invite">We graciously invite you and your family to join us for Bowling, Pizza and Drinks</p>
  </section>
</main>
</body>
</html>
```